Website for the new investment company.

We are building a website for a new company. This will be an investment company. The name of the company is Tern Harbor Equity, or THE. We don't have a company logo yet, so happy to take suggestions on that as well (and will add that to the final cost). The investors of this company will exclusively be Dunmore College alumni graduates. The investors are not students, but instead older professionals in various industries, that previously graduated from the Dunmore College. This company will establish an investment fund and invest in multiple businesses.
The purpose of the website will be to educate Dunmore alumni on the investment fund.
We are looking for:
1. The design to be relatable, but not the copy of the Dunmore College website. https://www.dunmorecol.edu/
2. This is an investment website and must mimic other similar websites
https://plovergate-fund.com/
https://www.brindlevest.com/
https://kestowholdings.com/site/global/home/p_home.gsp
3. Project timeline. We are focused on receiving a design in the next two weeks and then finishing the website over the following 2 weeks. We anticipate paying for additional work and customization after the designs are provided.
4. Website Pages:
1) Homepage - Mission and Objective (high quality photos along with text that we will provide after selecting the winning design)
2) Background - Text and biographies on the 2 founders (high quality photos along with text that we will provide after selecting the winning design)
3) Advisory Board - Text and biographies on the investment Fund's 3 advisory board members (high quality photos along with text that we will provide after selecting the winning design)
4) Fund I - Text and information on the specific investment fund including pictures and biographies of the investment committee (high quality photos along with text that we will provide after selecting the winning design)
5) Contact Us - Typical website contact page for visitors

Target Market(s)

Dunmore Alumni graduates

Industry/Entity Type

Investment

Coding

Coded - Design and coding required

Font styles to use
Serif
Sans Serif

Colors
0054AA
0677BA
7BADD7
CADEEF
E8F1F8

Requirements
Must have
• Must look like other private investment websites as provided in project description
Nice to have
• Mimics the Dunmore College style, but definitely needs to be different. This company has no direct relationship with Dunmore College.
Should not have
• No commercial transactions, no credit card payments etc. Do not replicate any logos, designs or proprietary content from Dunmore College.

```html
<!DOCTYPE html>
<html lang="en">
<head>
<meta charset="utf-8">
<title>Tern Harbor Equity</title>
<link rel="stylesheet" href="https://fonts.googleapis.com/css2?family=Open+Sans:wght@400;600;700&family=Playfair+Display:wght@600;700&display=swap">
<style>
:root{
  --deep:#0054AA;
  --mid:#0677BA;
  --soft:#7BADD7;
  --pale:#CADEEF;
  --mist:#E8F1F8;
  --ink:#1d2633;
  --white:#ffffff;
  --serif:"Playfair Display", Georgia, serif;
  --sans:"Open Sans", Arial, sans-serif;
}
*{box-sizing:border-box;margin:0;padding:0}
html,body{width:738px;height:1200px;overflow:hidden}
body{font-family:var(--sans);color:var(--ink);background:var(--white);position:relative}

.hero{position:absolute;left:0;top:0;width:738px;height:206px;overflow:hidden}
.hero-photo{position:absolute;inset:0;background:linear-gradient(180deg,#0a4f8f 0%,#0b6fc0 45%,#0a5ea8 100%)}
.hero-photo::after{content:"";position:absolute;inset:0;background:linear-gradient(90deg,rgba(0,40,90,.35) 0%,rgba(0,0,0,0) 40%,rgba(0,40,90,.3) 100%)}
.brand{position:absolute;left:38px;top:16px;display:flex;align-items:center;gap:5px;font-family:var(--sans);font-weight:700;color:var(--white);font-size:9px;letter-spacing:.3px}
.brand-mark{width:7px;height:7px;background:var(--white)}
.main-nav{position:absolute;left:266px;top:16px;display:flex;align-items:center;gap:0}
.main-nav a{font-size:5.6px;font-weight:700;color:var(--white);text-decoration:none;padding:4px 5px;letter-spacing:.1px}
.main-nav a.active{background:rgba(255,255,255,.22)}
.search-icon{margin-left:4px}
.hero-title{position:absolute;left:0;right:0;top:108px;text-align:center;font-family:var(--serif);font-weight:700;font-size:20.5px;color:var(--white)}

.intro{position:absolute;left:0;top:206px;width:738px;height:217px;background:linear-gradient(180deg,#ffffff 0%,#eef3f9 50%,#dfe8f3 100%)}
.intro-body{position:absolute;left:108px;top:36px;width:346px}
.intro-heading{font-family:var(--serif);font-weight:700;font-size:8.2px;color:var(--deep);margin-bottom:6px}
.intro-body p{font-size:6.5px;line-height:10.3px;margin-bottom:9.5px}
.intro-quote{position:absolute;left:462px;top:93px;width:164px;border-left:1.5px solid var(--soft);padding-left:10px;font-size:6.5px;line-height:10.3px;color:var(--deep)}

.split{position:absolute;left:0;width:738px;height:244px;display:flex}
.split.mission{top:423px}
.split.objectives{top:666px}
.split-photo{width:368px;height:244px;margin-left:1px}
.photo-observer{background:linear-gradient(180deg,#040c1f 0%,#0c2a55 40%,#1a4d8a 65%,#0a1d3a 100%)}
.photo-skyline{background:linear-gradient(180deg,#0a2c6e 0%,#0d3f8e 45%,#072a66 75%,#041a45 100%)}
.split-text{width:369px;height:244px;background:var(--mist);padding:20px 16px}
.split-text h2{font-family:var(--serif);font-weight:700;font-size:12.5px;color:var(--deep);margin-bottom:9px}
.split-text p{font-size:6.5px;line-height:10.3px}
.objective-list{padding-left:15px;font-size:6.5px;line-height:10.3px}
.objective-list strong{font-weight:700}

.tagline-band{position:absolute;left:0;top:910px;width:738px;height:112px;background:var(--mid);display:flex;align-items:center;justify-content:center}
.tagline-band p{font-family:var(--serif);font-weight:700;font-size:14px;color:var(--white)}

.site-footer{position:absolute;left:0;top:1022px;width:738px;height:178px;background:linear-gradient(120deg,#ffffff 0%,#f3f6fb 50%,#e6ecf9 100%)}
.footer-brand{position:absolute;left:0;right:0;top:49px;display:flex;justify-content:center;align-items:center;gap:6px;font-family:var(--sans);font-weight:700;font-size:12px;color:var(--deep)}
.footer-brand .brand-mark{width:9px;height:9px;background:var(--deep)}
.footer-nav{position:absolute;left:29px;top:107px;display:flex;gap:8px}
.footer-nav a{font-size:5.6px;font-weight:700;color:var(--deep);text-decoration:none}
.footer-contact{position:absolute;right:30px;top:107px;text-align:right;font-size:5px;line-height:8.3px;color:var(--deep)}
</style>
</head>
<body>

<header class="hero">
  <div class="hero-photo" role="img" aria-label="Blue-toned city skyline of tall office towers"></div>
  <div class="brand"><span class="brand-mark"></span>Tern Harbor Equity</div>
  <nav class="main-nav">
    <a class="active" href="#">HOME</a>
    <a href="#">BACKGROUND</a>
    <a href="#">ADVISORY BOARD</a>
    <a href="#">FUND I</a>
    <a href="#">CONTACT US</a>
    <svg class="search-icon" width="8" height="8" viewBox="0 0 10 10" aria-label="Search"><circle cx="4.2" cy="4.2" r="3.2" fill="none" stroke="#fff" stroke-width="1"/><line x1="6.6" y1="6.6" x2="9.2" y2="9.2" stroke="#fff" stroke-width="1"/></svg>
  </nav>
  <h1 class="hero-title">Tern Harbor Equity: Fueling Futures, Empowering Leaders</h1>
</header>

<section class="intro">
  <div class="intro-body">
    <h2 class="intro-heading">Building wealth with a focus on sustainable and ethical growth.</h2>
    <p>Welcome to Tern Harbor Equity, where our unwavering commitment to excellence drives every investment decision we make. At Tern Harbor Equity, we understand that true success is more than just financial gain; it’s about building a legacy of sustainable and ethical growth.</p>
    <p>Our approach is simple yet profound: we invest in select real estate developments and business ventures that align with our core values of integrity, innovation, and accountability. By partnering with us, you are not just investing in opportunities, but in a vision where excellence and success are intricately woven together.</p>
    <p>We pride ourselves on a hands-on approach, ensuring that each investment receives our full attention and expertise. Our mission is to add real value and help you achieve your financial goals while making a positive impact on the world.</p>
    <p>Join us in creating a future where wealth is built responsibly, and excellence is the fabric that binds us. This is the Tern Harbor Equity way.</p>
  </div>
  <blockquote class="intro-quote">Our investments are woven with the threads of unwavering pursuit, where excellence is the fabric, and success the natural tapestry it creates.</blockquote>
</section>

<section class="split mission">
  <div class="split-photo photo-observer" role="img" aria-label="Person seen from behind beside a telescope, looking out a window over a night city"></div>
  <div class="split-text">
    <h2>Mission Statement:</h2>
    <p>Our mission is to build a legacy of financial prosperity through unwavering commitment to excellence. We strive to deliver exceptional value to our investors by blending innovative strategies with ethical principles, fostering growth, and creating sustainable wealth.</p>
  </div>
</section>

<section class="split objectives">
  <div class="split-text" style="margin-left:1px">
    <h2>Objectives:</h2>
    <ol class="objective-list">
      <li><strong>Achieve Superior Financial Returns:</strong> Consistently outperform market benchmarks through meticulous analysis and strategic investments.</li>
      <li><strong>Ethical Investments:</strong> Prioritize investments that adhere to our core values of integrity, transparency, and social responsibility.</li>
      <li><strong>Client-Centered Approach:</strong> Provide personalized investment solutions tailored to meet the unique goals and risk tolerance of each investor.</li>
      <li><strong>Sustainable Growth:</strong> Focus on long-term growth by investing in sustainable and forward-thinking industries.</li>
      <li><strong>Continuous Improvement:</strong> Regularly review and refine our investment strategies to adapt to changing market conditions and maintain a competitive edge.</li>
    </ol>
  </div>
  <div class="split-photo photo-skyline" style="margin-left:0" role="img" aria-label="Downtown skyline lit up at night in deep blue tones"></div>
</section>

<section class="tagline-band">
  <p>Empowering your financial future through strategic investments.</p>
</section>

<footer class="site-footer">
  <div class="footer-brand"><span class="brand-mark"></span>Tern Harbor Equity</div>
  <nav class="footer-nav">
    <a href="#">HOME</a>
    <a href="#">BACKGROUND</a>
    <a href="#">ADVISORY BOARD</a>
    <a href="#">FUND I</a>
    <a href="#">PRIVACY POLICY</a>
    <a href="#">CONTACT US</a>
  </nav>
  <address class="footer-contact" style="font-style:normal">
    88 Meridian Way, Suite 300 Halden, TX 77010<br>
    Phone: (555) 014-2290<br>
    Email: hello@ternharborequity.com
  </address>
</footer>

</body>
</html>
```